Tri-fold Brochure Design for Banking Business

The brochure we have needs to be improved - more business like and more attractive. Logo file and brochure is attached. I would like to be able to edit the text after you get done. Your ideas and changes to text are welcome. See our website www.korvanbridgegrp.com for our theme. We can use indesign to edit the text after you complete. However, please make changes to the text we have in the design that it uploaded. Your comments and changes are welcome.

Target Market(s)

Human Resources and learning & development staff at the global investment banks - Pellham Trask, QWNR, etc.

Industry/Entity Type

Investment Banking

Logo Text

Korvan Bridge Group

Font styles to use
Serif
Sans Serif

Colors
33a6d7
0493ce
3277b5
fbf289
fdf9cf
fbee3e
0555a3
85acd3

Requirements
Must have
• Must be similar to our website www.korvanbridgegrp.com. Needs to be business-like, clean fonts, sharp design. Our logo - of course.
Nice to have
• City images - seems to be our theme.

```html
<!DOCTYPE html>
<html lang="en">
<head>
<meta charset="utf-8">
<title>Korvan Bridge Group – Tri-fold Brochure</title>
<link href="https://fonts.googleapis.com/css2?family=Jost:wght@400;500;600;700&display=swap" rel="stylesheet">
<style>
  :root{
    --yellow:#f2c418;
    --yellow-box:#e8b623;
    --navy:#0d3f8f;
    --blue:#0555a3;
    --ink:#27313d;
    --white:#ffffff;
    --page:#e9ebee;
  }
  *{margin:0;padding:0;box-sizing:border-box}
  html,body{width:1200px;height:800px;overflow:hidden;background:var(--page);font-family:'Jost',sans-serif}
  .brochure{position:absolute;left:30px;top:30px;width:1140px;height:740px;display:flex;box-shadow:0 6px 24px rgba(0,0,0,.18)}
  .panel{position:relative;width:380px;height:740px;overflow:hidden}

  /* panel 1 */
  .panel--about{background:var(--white)}
  .about__title{position:absolute;left:40px;top:60px;font-size:26px;font-weight:400;color:var(--ink);letter-spacing:.5px}
  .about__title strong{color:var(--blue);font-weight:700}
  .about__rule{position:absolute;left:40px;top:104px;width:260px;height:2px;background:var(--yellow)}
  .about__text{position:absolute;left:40px;top:124px;width:300px;font-size:13.5px;line-height:1.45;color:var(--ink)}
  .about__text p{margin-bottom:10px}
  .about__photo{position:absolute;left:40px;top:330px;width:300px;height:300px;background:linear-gradient(180deg,#3d5f86 0%,#5a7ea3 45%,#c9896a 78%,#1c2636 100%)}
  .about__accent{position:absolute;right:0;top:380px;width:42px;height:170px;background:var(--yellow-box)}

  /* bands */
  .band{position:absolute;left:0;bottom:0;width:100%;height:70px;display:flex;align-items:center;justify-content:center;font-size:18px;font-weight:600;letter-spacing:.3px}
  .band--yellow{background:var(--yellow);color:var(--navy)}
  .band--blue{background:var(--navy);color:var(--white)}

  /* panel 2 */
  .panel--contact{background:#1b2433}
  .contact__scene{position:absolute;inset:0;background:linear-gradient(180deg,#2a3447 0%,#4a4e58 30%,#6d6258 55%,#2b3038 100%)}
  .contact__heading{position:absolute;left:40px;top:250px;color:var(--white)}
  .contact__heading .lead{display:block;font-size:26px;font-weight:700;color:var(--yellow);letter-spacing:.5px}
  .contact__heading .rest{display:block;font-size:26px;font-weight:400;letter-spacing:.5px}
  .contact__touch{position:absolute;left:40px;top:390px;font-size:22px;font-weight:600;color:var(--white);letter-spacing:1px}
  .contact__box{position:absolute;left:0;top:430px;width:380px;height:200px;background:var(--yellow-box);padding:20px 24px 0 40px;color:var(--ink)}
  .contact__item{margin-bottom:8px}
  .contact__region{display:block;font-size:13px;font-weight:700;letter-spacing:.5px}
  .contact__email{display:block;font-size:13px}

  /* panel 3 */
  .panel--cover{background:#8aa4bd}
  .cover__photo{position:absolute;inset:0;background:linear-gradient(180deg,#9fb9d3 0%,#7d8ea0 35%,#8a6a4e 60%,#3a3f47 100%)}
  .cover__logo{position:absolute;left:40px;top:36px;display:flex;align-items:center;gap:10px;background:rgba(255,255,255,.9);padding:8px 14px}
  .cover__logo-mark{width:22px;height:22px;background:var(--yellow)}
  .cover__logo-name{font-size:20px;font-weight:600;color:var(--ink);letter-spacing:.5px}
  .cover__claim{position:absolute;left:40px;top:430px;width:320px;height:180px;background:var(--navy);padding:26px 26px;opacity:.95}
  .cover__claim .big{display:block;font-size:34px;font-weight:700;color:var(--yellow);line-height:1.05}
  .cover__claim .mid{display:block;font-size:20px;font-weight:500;color:var(--white);line-height:1.2;margin:4px 0}
</style>
</head>
<body>
<main class="brochure">

  <section class="panel panel--about">
    <h2 class="about__title">ABOUT <strong>US</strong></h2>
    <div class="about__rule"></div>
    <div class="about__text">
      <p>Korvan Bridge Group efficiently provides complete sales, marketing and logistical support for all our programs, no matter the location.</p>
      <p>Our globally located trainers have extensive experience, both as industry professionals and as trainers.</p>
      <p>Our highly qualified logistical team complement the training services, providing reliable and efficient support.</p>
    </div>
    <div class="about__photo" role="img" aria-label="Business district skyscrapers at dusk"></div>
    <div class="about__accent"></div>
    <div class="band band--yellow">www.korvanbridgegrp.com</div>
  </section>

  <section class="panel panel--contact">
    <div class="contact__scene" role="img" aria-label="City skyline at sunset with a line-drawn world map above"></div>
    <h2 class="contact__heading"><span class="lead">WORLDWIDE</span><span class="rest">TRAINING SERVICE</span></h2>
    <h3 class="contact__touch">GET IN TOUCH</h3>
    <div class="contact__box">
      <div class="contact__item"><span class="contact__region">GLOBAL:</span><span class="contact__email">nadia.verlotti@korvanbridgegrp.com</span></div>
      <div class="contact__item"><span class="contact__region">ASIA:</span><span class="contact__email">owen.pellard@korvanbridgegrp.com</span></div>
      <div class="contact__item"><span class="contact__region">UNITED STATES:</span><span class="contact__email">peter.calvane@korvanbridgegrp.com</span></div>
      <div class="contact__item"><span class="contact__region">EUROPE:</span><span class="contact__email">simon.ketterly@korvanbridgegrp.com</span></div>
    </div>
    <div class="band band--blue">www.korvanbridgegrp.com</div>
  </section>

  <section class="panel panel--cover">
    <div class="cover__photo" role="img" aria-label="Downtown skyscrapers in daylight seen from above"></div>
    <div class="cover__logo">
      <span class="cover__logo-mark"></span>
      <span class="cover__logo-name">KORVAN BRIDGE GROUP</span>
    </div>
    <h1 class="cover__claim">
      <span class="big">YOUR</span>
      <span class="mid">EXPERT TRAINING<br>AND CONSULTING</span>
      <span class="big">PARTNER</span>
    </h1>
    <div class="band band--yellow">www.korvanbridgegrp.com</div>
  </section>

</main>
</body>
</html>
```